(Wordpress)Website Design - No requirements! Sign Your name at the bottom of the site!

Dear Designer,

I am looking for a designer who is interested in a long-term business realtionship.
I already have 2 more designs to get done IMMEDIATELY after this website..
1.) An email brochure matching the website theme.
2.) A Billboard. BOTH MATCHING THE WEBSITE THEME

For this project, a bonus WILL be given.

Go to vaultmoor.com as Site Inspiration

Please take this opportunity to design an existing wordpress website, FUNDSWIFTLANE.com, in whatever form your creativity takes you

I have no requirements other than a CREATIVE and OUT-OF -THE-BOX Design. Something Pretty and Eye Catching; a website that someone logs onto and doesnt want to leave

I have purchased a theme called lumetra. You dont need to use it...But Info can be found at

http://skinbazaar.example/item/lumetra-premium-wordpress-theme/full_screen_preview/572046

I have attached my logos and a PDF with a short story about what our company does.

Thank You,
-Tobin
PS I HAVE ANOTHER 2 DESIGNS TO DO AFTER THIS PROJECT.
also, IF YOU KNOW OF SOMEONE WHO DOES SEO WORK, I AM LOOKING FOR A FULL-TIME EMPLOYEE

Target Market(s)

Business Owners in a state of finacial NEED

Industry/Entity Type

Business

Requirements
Must have
• COLORFUL, EYE CATCHING

```html
<!DOCTYPE html>
<html lang="en">
<head>
<meta charset="utf-8">
<title>Swiftlane Capital</title>
<link rel="stylesheet" href="https://fonts.googleapis.com/css2?family=Source+Sans+3:wght@400;600;700&family=PT+Sans+Narrow:wght@400;700&family=Questrial&family=Oswald:wght@300;400&family=Open+Sans:wght@400&display=swap">
<style>
:root{
  --ink:#1c1c1c;
  --band:#1a1a1a;
  --blue:#0a5aa0;
  --blue-deep:#003f7a;
  --blue-head:#0b5ea8;
  --grey-text:#666;
  --step-text:#777;
  --panel:#3a3a3a;
  --btn-grey:#b9b9b9;
  --green:#6cb33f;
}
*{margin:0;padding:0;box-sizing:border-box}
html,body{width:1123px;height:1200px;overflow:hidden;background:#fff}
body{position:relative;font-family:"Source Sans 3",sans-serif;color:var(--ink)}
.abs{position:absolute}
.header-band{left:0;top:0;width:1123px;height:246px;background:linear-gradient(#262626,#161616)}
.brand{left:125px;top:14px;display:flex;align-items:center;gap:8px;color:#6fa8dc;font-size:27px;font-weight:600;letter-spacing:-.5px}
.brand-dot{width:26px;height:26px;border-radius:50%;background:#6fa8dc}
.nav{left:132px;top:68px;display:flex;font-size:13px;color:#fff;letter-spacing:-.3px}
.nav a{color:#fff;text-decoration:none;position:absolute;top:0;white-space:nowrap}
.nav .active{background:var(--blue);padding:0 5px;top:0;line-height:17px}
.login{left:699px;top:0;width:292px;height:82px;background:var(--blue);color:#fff}
.login .field{position:absolute;top:10px;height:17px;background:#fff;color:#222;font-size:10px;padding:2px 8px}
.login .go{position:absolute;left:235px;top:10px;width:49px;height:17px;background:#6a9fd1;font-size:10px;padding:2px 0 0 18px;color:#fff}
.login .small{position:absolute;top:33px;font-size:9px}
.login .call{position:absolute;left:19px;top:55px;font-size:13px;font-weight:600}
.hero{left:132px;top:105px;width:859px;height:333px;background:linear-gradient(100deg,#9fb6c9 0%,#c9d5de 45%,#e2e6ea 70%,#8a8f96 100%)}
.hero-person{left:690px;top:105px;width:301px;height:333px;background:linear-gradient(180deg,#c8a48c 0%,#b0887a 45%,#1d1d22 70%,#121216 100%)}
.hero-copy{left:445px;top:120px;color:#fff;text-shadow:0 1px 3px rgba(0,0,0,.45)}
.hero-copy h1{font-family:"Source Sans 3",sans-serif;font-size:38px;font-weight:700;letter-spacing:-1.5px;line-height:40px}
.hero-copy p{font-size:14.5px;line-height:20px;letter-spacing:-.4px}
.hero-copy ul{list-style:none;margin-top:8px}
.hero-copy li{font-size:16.5px;font-weight:600;letter-spacing:-.6px;line-height:24.5px;display:flex;align-items:center;gap:8px}
.hero-copy li svg{flex:none}
.dots{left:522px;top:406px;display:flex;gap:9px}
.dots span{width:9px;height:9px;border-radius:50%;background:#222}
.dots .on{background:#fff;border:2px solid #222;width:11px;height:11px;margin-top:-1px}
.form-panel{left:115px;top:129px;width:312px;height:279px;background:linear-gradient(135deg,rgba(58,58,58,.96),rgba(78,78,78,.92))}
.form-fold{left:115px;top:408px;width:0;height:0;border-top:16px solid #111;border-left:16px solid transparent}
.form-notch{left:240px;top:408px;width:70px;height:30px;background:#666;clip-path:polygon(0 0,100% 0,80% 100%,20% 100%)}
.input{position:absolute;left:16px;width:231px;height:28px;background:#fff;border:1px solid #ccc;font-family:"PT Sans Narrow",sans-serif;font-size:9px;color:#888;padding:8px 10px;text-transform:uppercase}
.agree{position:absolute;left:19px;top:222px;color:#fff;font-family:"PT Sans Narrow",sans-serif;font-weight:700;font-size:16px;display:flex;align-items:center;gap:4px}
.submit{position:absolute;left:102px;top:245px;width:107px;height:26px;background:var(--blue);color:#fff;font-size:15px;font-weight:600;letter-spacing:-.5px;display:flex;align-items:center;justify-content:center;gap:12px}
.apply-vert{position:absolute;left:265px;top:275px;color:#fff;font-family:"Oswald",sans-serif;font-weight:300;font-size:34px;letter-spacing:1px;transform:rotate(-90deg);transform-origin:left top;white-space:nowrap}
.hero-shadow{left:150px;top:438px;width:823px;height:40px;background:radial-gradient(ellipse at top,rgba(0,0,0,.35),rgba(0,0,0,0) 70%)}
.pitch{left:0;top:490px;width:1123px;text-align:center}
.pitch .h{color:var(--blue-head);white-space:nowrap}
.pitch .lead{font-size:34px;font-weight:600;letter-spacing:-2px}
.pitch .rest{font-family:"PT Sans Narrow",sans-serif;font-weight:700;font-size:27px;letter-spacing:-.2px}
.pitch .sub{font-family:"Questrial",sans-serif;font-size:21px;color:#111;margin-top:0}
.rule{left:300px;width:523px;height:18px;background:radial-gradient(ellipse at top,rgba(0,0,0,.12),rgba(0,0,0,0) 70%);border-top:1px solid #ddd}
.step-num{font-size:15px;font-weight:600;color:#444}
.step-label{font-size:17px;color:var(--step-text);letter-spacing:-.6px;line-height:24.5px}
.step-btn{width:105px;height:29px;color:#fff;font-size:17px;font-weight:600;letter-spacing:-.8px;display:flex;align-items:center;justify-content:center}
.step-btn.primary{background:linear-gradient(#1f6bb0,#063f78)}
.step-btn.muted{background:linear-gradient(#d0d0d0,#a8a8a8)}
.clock{border-radius:50%;background:radial-gradient(circle,#fff 45%,#9a9a9a 60%,#5f5f5f 100%)}
.bar-title{height:42px;color:#fff;font-family:"PT Sans Narrow",sans-serif;font-weight:700;font-size:28px;padding:4px 0 0 9px;letter-spacing:-.2px}
.welcome-bar{left:132px;top:826px;width:478px;background:linear-gradient(90deg,#0d0d0d 55%,rgba(13,13,13,0) 100%)}
.testi-bar{left:619px;top:826px;width:276px;background:linear-gradient(90deg,#0d0d0d 55%,rgba(13,13,13,0) 100%)}
.welcome-text{left:141px;top:884px;width:412px;font-family:"Open Sans",sans-serif;font-size:11.5px;line-height:24.6px;color:var(--grey-text);text-align:justify}
.quote-box{left:619px;top:887px;width:291px;height:135px;background:var(--blue-deep);color:#fff;padding:0 20px 0 28px;box-shadow:0 6px 6px -4px rgba(0,0,0,.35)}
.quote-box h3{font-family:"Open Sans",sans-serif;font-weight:400;font-size:22px;margin-top:21px}
.quote-box p{font-size:9px;line-height:14.5px;margin-top:4px}
.qmark{position:absolute;font-family:Georgia,serif;font-weight:700;font-size:32px;line-height:1;color:#dfe8f3}
.subscribe-input{left:702px;top:1035px;width:146px;height:20px;border:1px solid #aaa;border-radius:3px;background:linear-gradient(#eee,#ddd);font-size:8px;font-style:italic;color:#555;padding:4px 8px}
.subscribe-btn{left:859px;top:1034px;width:51px;height:22px;border-radius:4px;background:linear-gradient(#8fa3b3,#5f7486);color:#fff;font-family:"PT Sans Narrow",sans-serif;font-weight:700;font-size:10px;display:flex;align-items:center;justify-content:center}
.footer-rule{left:150px;top:1130px;width:823px;height:14px;border-top:1px solid #ddd;background:radial-gradient(ellipse at top,rgba(0,0,0,.08),rgba(0,0,0,0) 70%)}
.footer-nav{left:0;top:1142px;width:1123px;display:flex;justify-content:center;gap:20px;font-size:12px;font-weight:600;letter-spacing:-.5px;color:#111}
.copyright{left:0;top:1164px;width:1123px;text-align:center;font-size:11.5px;letter-spacing:-.5px;color:#222}
</style>
</head>
<body>
<div class="abs header-band"></div>

<div class="abs brand"><span class="brand-dot"></span>Swiftlane Capital</div>

<nav class="abs nav">
  <a class="active" style="left:0">Home</a>
  <a style="left:78px">About us</a>
  <a style="left:164px">Services</a>
  <a style="left:249px">FAQ'S</a>
  <a style="left:321px">Our Advantage</a>
  <a style="left:443px">Contact us</a>
</nav>

<div class="abs login">
  <div class="field" style="left:12px;width:103px">Email:</div>
  <div class="field" style="left:123px;width:102px">Password</div>
  <div class="go">Login</div>
  <svg class="abs" style="left:241px;top:13px" width="8" height="10" viewBox="0 0 8 10"><circle cx="4" cy="3" r="2.3" fill="#fff"/><path d="M0 10 Q4 4 8 10Z" fill="#fff"/></svg>
  <div class="small" style="left:14px">Keep me Logged in <span style="display:inline-block;width:9px;height:7px;background:#fff;border-radius:2px;vertical-align:middle"></span></div>
  <div class="small" style="left:123px;text-decoration:underline">Forgot your password</div>
  <div class="call">Begin Online Or Call Us Now! (800)555-0142</div>
</div>

<div class="abs hero" role="img" aria-label="Office background scene"></div>
<div class="abs hero-person" role="img" aria-label="Smiling businesswoman in a dark suit"></div>

<div class="abs hero-copy">
  <h1>APPLY TODAY!</h1>
  <p>For an instant Swiftlane Capital with Quick Draw<br>Apply in your web browser or on your cell phone</p>
  <ul>
    <li><svg width="14" height="14" viewBox="0 0 14 14"><rect x="1" y="3" width="10" height="10" fill="#fff" opacity=".85"/><path d="M3 8 L6 11 L13 1" stroke="#333" stroke-width="2" fill="none"/></svg>Instant Transfer</li>
    <li><svg width="14" height="14" viewBox="0 0 14 14"><rect x="1" y="3" width="10" height="10" fill="#fff" opacity=".85"/><path d="M3 8 L6 11 L13 1" stroke="#333" stroke-width="2" fill="none"/></svg>Instant Decision</li>
    <li><svg width="14" height="14" viewBox="0 0 14 14"><rect x="1" y="3" width="10" height="10" fill="#fff" opacity=".85"/><path d="M3 8 L6 11 L13 1" stroke="#333" stroke-width="2" fill="none"/></svg>Safe &amp; Secure</li>
    <li><svg width="14" height="14" viewBox="0 0 14 14"><rect x="1" y="3" width="10" height="10" fill="#fff" opacity=".85"/><path d="M3 8 L6 11 L13 1" stroke="#333" stroke-width="2" fill="none"/></svg>Choose Your Amount</li>
  </ul>
</div>

<div class="abs dots"><span class="on"></span><span></span><span></span><span></span><span></span></div>

<div class="abs form-notch"></div>
<div class="abs form-fold"></div>
<form class="abs form-panel">
  <div class="input" style="top:16px">First name:</div>
  <div class="input" style="top:70px">Last name</div>
  <div class="input" style="top:124px">Email</div>
  <div class="input" style="top:179px">Phone</div>
  <div class="agree"><svg width="12" height="12" viewBox="0 0 12 12"><rect width="12" height="12" fill="#fff"/><path d="M2 6 L5 9 L10 2" stroke="#333" stroke-width="2" fill="none"/></svg>"I AGREE TO TERMS AND CONDITIONS"</div>
  <div class="submit">SUBMIT <svg width="7" height="11" viewBox="0 0 7 11"><path d="M1 1 L6 5.5 L1 10" stroke="#fff" stroke-width="1.8" fill="none"/></svg></div>
  <div class="apply-vert">APPLY NOW!</div>
</form>

<div class="abs hero-shadow"></div>

<section class="abs pitch">
  <div class="h"><span class="lead">No Credit Check!</span> <span class="rest">Be Up to $1,500 Richer in Less Than 1 Hour!</span></div>
  <div class="sub">All you need is a checking account approval is guaranteed!</div>
</section>

<div class="abs rule" style="top:587px"></div>

<!-- steps -->
<div class="abs step-num" style="left:161px;top:645px">1.</div>
<div class="abs clock" style="left:201px;top:625px;width:56px;height:70px;border-radius:45%" role="img" aria-label="Alarm clock"></div>
<div class="abs step-label" style="left:277px;top:645px">Apply For<br>Money</div>
<div class="abs step-btn primary" style="left:252px;top:709px">Apply Now!</div>

<div class="abs step-num" style="left:436px;top:645px">2.</div>
<svg class="abs" style="left:486px;top:650px" width="42" height="36" viewBox="0 0 42 36"><path d="M3 18 L15 30 L39 4" stroke="var(--green)" stroke-width="8" fill="none" stroke-linecap="round" stroke-linejoin="round"/></svg>
<div class="abs step-label" style="left:553px;top:645px">Get<br>Approved</div>
<div class="abs step-btn muted" style="left:527px;top:709px">Apply Now!</div>

<div class="abs step-num" style="left:702px;top:645px">3.</div>
<svg class="abs" style="left:742px;top:637px" width="55" height="55" viewBox="0 0 55 55"><circle cx="27.5" cy="27.5" r="27" fill="var(--green)"/><text x="27.5" y="39" text-anchor="middle" font-family="Source Sans 3, sans-serif" font-weight="700" font-size="34" fill="#fff">$</text></svg>
<div class="abs step-label" style="left:819px;top:645px">Receive<br>Your Money</div>
<div class="abs step-btn muted" style="left:793px;top:709px">Apply Now!</div>

<div class="abs rule" style="top:789px;left:132px;width:859px"></div>

<h2 class="abs bar-title welcome-bar">Welcome to Swiftlane Capital</h2>
<h2 class="abs bar-title testi-bar">Client Testimonials</h2>

<p class="abs welcome-text">Lorem Ipsum is simply dummy text of the printing and typesetting industry. Lorem Ipsum has been the industry's standard dummy text ever since the 1500s, when an unknown printer took a galley of type and scrambled it to make a type specimen book. It has survived not only five centuries, but also the leap into electronic typesetting, remaining essentially unchanged. It was popularised in the 1960s with the release of Letterkit sheets containing Lorem Ipsum passages, and more recently with desktop publishing software like Pagewright including versions of Lorem Ipsum.</p>

<svg class="abs" style="left:593px;top:950px" width="12" height="18" viewBox="0 0 12 18"><path d="M10 2 L3 9 L10 16" stroke="#aaa" stroke-width="3" fill="none"/></svg>
<svg class="abs" style="left:919px;top:950px" width="12" height="18" viewBox="0 0 12 18"><path d="M2 2 L9 9 L2 16" stroke="#aaa" stroke-width="3" fill="none"/></svg>

<blockquote class="abs quote-box">
  <span class="qmark" style="left:5px;top:6px">&ldquo;</span>
  <h3>Dara Venn</h3>
  <p>lacus, vel posuere felis. Curabitur bibendum vestibulum lorem, eget tempor piscing nisi. In congue justo a libero ullamcorper aliquet. Quisque gravida, justo ac tempor congue, nibh magna mattis felis, ut tempus ms. Integer sit amet.</p>
  <span class="qmark" style="left:264px;top:110px">&rdquo;</span>
</blockquote>

<div class="abs subscribe-input">Enter your email to recive updates...</div>
<div class="abs subscribe-btn">SUBSCRIBE</div>

<div class="abs footer-rule"></div>
<nav class="abs footer-nav"><span>Home</span><span>About us</span><span>Services</span><span>FAQ'S</span><span>Our Advantage</span><span>Contact us</span></nav>
<div class="abs copyright">Copy Rights 2012</div>
</body>
</html>
```